need a clean, modern job advertisement designed for social media (Facebook & Instagram).

The post is to advertise two positions:
• Leading Hand Boilermaker
• Dragline Fitter
We want the design to match our KRT Plant Services branding: blue, white, strong, professional, mining-industry style.
What the design should include:
Bold headline: “WE’RE HIRING”
Sub-headline: “Leading Hand Boilermaker & Dragline Fitter”
Key points:
• Bowen Basin based
• Dragline & shovel maintenance
• Great pay + long-term work
• Locally owned & operated
KRT logo placed cleanly
Space for 1–2 images (boilermaking or dragline work)
Design style:
Strong and industrial
Blue/white colour scheme
Easy to read at a glance
Suitable for a square 1080×1080 design

```html
<!DOCTYPE html>
<html lang="en">
<head>
<meta charset="utf-8">
<title>KRT Plant Services – We're Hiring</title>
<link href="https://fonts.googleapis.com/css2?family=Barlow+Condensed:wght@800&family=Catamaran:wght@600;700&display=swap" rel="stylesheet">
<style>
  :root {
    --brand-blue: #42ade2;
    --brand-blue-light: #9fd3f1;
    --ink: #050505;
    --white: #ffffff;
    --stage: #ededed;
    --photo-dark: #120c08;
    --photo-mid: #3b2a1d;
    --photo-warm: #5e4228;
  }
  * { margin: 0; padding: 0; box-sizing: border-box; }
  html, body {
    width: 1200px; height: 1117px; overflow: hidden;
    background: var(--stage);
  }
  .post {
    position: absolute; left: 41.5px; top: 0;
    width: 1395px; height: 1394px;
    transform: scale(0.8007); transform-origin: top left;
    overflow: hidden;
    font-family: "Catamaran", "Helvetica Neue", Arial, sans-serif;
  }
  .post-shapes { position: absolute; inset: 0; }
  .brand-mark {
    position: absolute; left: 40px; top: 215px; width: 620px;
    display: flex; align-items: center; justify-content: center; gap: 20px;
    color: var(--brand-blue); font-weight: 700; font-size: 66px; line-height: 1;
  }
  .brand-mark .dot {
    width: 40px; height: 40px; border-radius: 50%; background: var(--brand-blue);
    flex: none;
  }
  .headline {
    position: absolute; left: 170px; top: 545px; width: 1060px;
    text-align: center; color: var(--white);
    font-family: "Barlow Condensed", "Arial Narrow", sans-serif;
    font-weight: 800; font-size: 212px; line-height: 1; letter-spacing: 1px;
    text-shadow: 4px 5px 0 rgba(0,0,0,0.12);
  }
  .subhead {
    position: absolute; left: 150px; top: 762px; width: 1090px;
    text-align: center; color: var(--white);
    font-weight: 600; font-size: 65px; line-height: 63px;
  }
  .perks {
    position: absolute; top: 976px; list-style: none;
    color: var(--white); font-weight: 600; font-size: 44px; line-height: 45px;
  }
  .perks li { position: relative; padding-left: 58px; margin-bottom: 22px; }
  .perks li svg { position: absolute; left: 0; top: 4px; width: 34px; height: 34px; }
  .perks-left { left: 165px; }
  .perks-right { left: 747px; }
  .perks-divider {
    position: absolute; left: 697px; top: 976px; width: 2px; height: 202px;
    background: #555;
  }
  .web-link {
    position: absolute; left: 310px; top: 1262px; width: 790px; height: 92px;
    display: flex; align-items: center; justify-content: center; gap: 26px;
    color: var(--white); font-weight: 700; font-size: 64px; line-height: 1;
  }
  .web-link svg { width: 46px; height: 46px; flex: none; }
</style>
</head>
<body>
<main class="post">
  <svg class="post-shapes" viewBox="0 0 1395 1394" width="1395" height="1394">
    <defs>
      <linearGradient id="paper" x1="0" y1="0" x2="1" y2="1">
        <stop offset="0" stop-color="#e4e6e8"/>
        <stop offset="0.5" stop-color="#f7f7f8"/>
        <stop offset="1" stop-color="#e9eaec"/>
      </linearGradient>
      <radialGradient id="photo" cx="0.55" cy="0.45" r="0.7">
        <stop offset="0" stop-color="var(--photo-warm)"/>
        <stop offset="0.45" stop-color="var(--photo-mid)"/>
        <stop offset="1" stop-color="var(--photo-dark)"/>
      </radialGradient>
      <linearGradient id="faded-photo" x1="0" y1="0" x2="1" y2="0">
        <stop offset="0.4" stop-color="#050505"/>
        <stop offset="1" stop-color="#333333"/>
      </linearGradient>
      <linearGradient id="stripe" x1="0" y1="0" x2="0" y2="1">
        <stop offset="0" stop-color="var(--brand-blue)"/>
        <stop offset="1" stop-color="var(--brand-blue)" stop-opacity="0"/>
      </linearGradient>
      <linearGradient id="banner" x1="0" y1="0" x2="1" y2="0">
        <stop offset="0" stop-color="var(--brand-blue-light)"/>
        <stop offset="0.12" stop-color="var(--brand-blue)"/>
        <stop offset="0.88" stop-color="var(--brand-blue)"/>
        <stop offset="1" stop-color="var(--brand-blue-light)"/>
      </linearGradient>
    </defs>

    <rect class="top-panel" x="0" y="0" width="1395" height="727" fill="url(#paper)"/>
    <g class="paper-facets" fill="#ffffff" opacity="0.55">
      <polygon points="0,0 80,0 0,260"/>
      <polygon points="180,0 560,0 320,240"/>
      <polygon points="0,470 90,420 260,620 180,700 0,700"/>
    </g>
    <polygon class="accent-stripe" points="738,0 823,0 603,700 540,700" fill="url(#stripe)"/>
    <polygon class="hero-photo" role="img" aria-label="Photo of a boilermaker welding inside a dragline, sparks flying"
             points="823,0 1395,0 1395,700 603,700" fill="url(#photo)"/>

    <rect class="blue-rule" x="0" y="700" width="1395" height="27" fill="var(--brand-blue)"/>
    <rect class="info-panel" role="img" aria-label="Faded photo of dragline boom steelwork"
          x="0" y="727" width="1395" height="502" fill="url(#faded-photo)"/>

    <polygon class="headline-banner" points="163,529 1328,529 1233,924 66,924" fill="url(#banner)"/>

    <rect class="bottom-panel" x="0" y="1229" width="1395" height="133" fill="url(#paper)"/>
    <rect class="bottom-bar" x="0" y="1362" width="1395" height="32" fill="var(--brand-blue)"/>
    <polygon class="web-tab" points="320,1255 1073,1255 1118,1363 278,1363" fill="var(--brand-blue)"/>
  </svg>

  <div class="brand-mark"><span class="dot"></span>KRT Plant Services</div>

  <h1 class="headline">WE’RE HIRING</h1>
  <p class="subhead">LEADING HAND BOILERMAKER<br>&amp; DRAGLINE FITTER</p>

  <ul class="perks perks-left">
    <li><svg viewBox="0 0 34 34"><circle cx="17" cy="17" r="17" fill="#fff"/><path d="M9 17.5l5.5 5.5L25 12" fill="none" stroke="#050505" stroke-width="4" stroke-linecap="round" stroke-linejoin="round"/></svg>BOWEN BASIN BASED</li>
    <li><svg viewBox="0 0 34 34"><circle cx="17" cy="17" r="17" fill="#fff"/><path d="M9 17.5l5.5 5.5L25 12" fill="none" stroke="#050505" stroke-width="4" stroke-linecap="round" stroke-linejoin="round"/></svg>DRAGLINE &amp; SHOVEL<br>MAINTENANCE</li>
  </ul>
  <div class="perks-divider"></div>
  <ul class="perks perks-right">
    <li><svg viewBox="0 0 34 34"><circle cx="17" cy="17" r="17" fill="#fff"/><path d="M9 17.5l5.5 5.5L25 12" fill="none" stroke="#050505" stroke-width="4" stroke-linecap="round" stroke-linejoin="round"/></svg>LOCALLY OWNED &amp;<br>OPERATED</li>
    <li><svg viewBox="0 0 34 34"><circle cx="17" cy="17" r="17" fill="#fff"/><path d="M9 17.5l5.5 5.5L25 12" fill="none" stroke="#050505" stroke-width="4" stroke-linecap="round" stroke-linejoin="round"/></svg>GREAT PAY +<br>LONG-TERM WORK</li>
  </ul>

  <div class="web-link">
    <svg viewBox="0 0 44 44"><circle cx="22" cy="22" r="22" fill="#fff"/><g fill="none" stroke="var(--brand-blue)" stroke-width="2"><circle cx="22" cy="22" r="11"/><ellipse cx="22" cy="22" rx="5" ry="11"/><path d="M11 22h22M13 16h18M13 28h18"/></g></svg>
    krtplantservices.com
  </div>
</main>
</body>
</html>
```